Jewelry webpage design project

Velmora is an Online-shop committed to keep the natural beauty of the flowers as jewelry or accessories for women and kids.

Our products are miniaturized flowers kept in transparent resin and assembled on sterling silver. All jewelry and accessories pieces are handmade.

Target market are women who are used to buy per internet from 25 to 45 years old and men who send surprise presents from 25 to 55.
Velmora focuses on the European market, with Germany and Austria as primary customers.

The design of the webpage will have to express the following principles:
• Not complicated but elegant and trustworthy
• Friendly and easy to surf and use
• Express the slogan “beautiful by nature”
• Has to match or flow with the attached logo (doesn’t have to include the same colors)
• Adjust the design to “create the experience” of picking flowers in a garden or silver garden.

As an extra service we will offer special packaging for presents or special events. This option has to be very distinctive or perceptible. The customer have to be able to select the packaging when performing check out.

We are open to any layout but as a guide of how “friendly to use” it has to be, reference attachments are included ( logo, proposed layouts and jewelry photos).

Ecommerce platform will be osCommerce. Within the design proposals hover actions (e.g at menu, links or images) must be shown. No flash application is intended. Image menus are desirable.

Design proposals should include the following layouts:
Main Page
Category Page
Product Page
Packaging Selection (before Checkout)
Checkout Page

*** As an extra Info on the packaging, it is very important to know that we will offer three different packaging options to choose from: the normal one (no extra charges), the one for special occasions (anniversary, Valentine´s day, etc.) and one for birthday presents, both with extra charges.

Target Market(s)

Target market are women from 25 to 45 years old and men who send surprise presents from 25 to 55.

Industry/Entity Type

Internet

Requirements
Must have
• Design proposals should include the following layouts:
- Main Page
- Category Page
- Product Page
- Packaging Selection (before Checkout)
- Checkout Page

Hover actions and transitions (e.g at menu, links or images) must be shown
Nice to have
• Image menus are desirable.
e.g. http://www.quibrendalweb.net/examples/image-menu-1.html
Should not have
• Adobe Flash proposal

```html
<!DOCTYPE html>
<html lang="en">
<head>
<meta charset="utf-8">
<title>Velmora – Checkout</title>
<link href="https://fonts.googleapis.com/css2?family=Quicksand:wght@500;700&family=Arimo:wght@400;700&family=Niconne&display=swap" rel="stylesheet">
<style>
:root{
  --plum:#7d1760;
  --plum-deep:#86186a;
  --green:#7ab317;
  --ink:#333333;
  --muted:#8a8a8a;
  --field:#ececec;
  --field-line:#d6d6d6;
  --header-bg:#f3f3f3;
  --white:#ffffff;
  --error:#e3625e;
  --card:#d9d9d9;
}
*{box-sizing:border-box;margin:0;padding:0}
html,body{width:1117px;height:1200px;overflow:hidden;background:var(--white)}
body{position:relative;font-family:"Arimo",Arial,sans-serif;color:var(--ink)}
.abs{position:absolute}

/* header */
.top-rule{left:0;top:0;width:1117px;height:5px;background:var(--plum)}
.site-header{left:0;top:5px;width:1117px;height:163px;background:var(--header-bg);border-bottom:1px solid #e0e0e0;box-shadow:0 2px 4px rgba(0,0,0,.06)}
.brand{left:112px;top:74px;display:flex;align-items:center;gap:12px}
.brand-mark{width:14px;height:14px;background:var(--plum)}
.brand-name{font-family:"Quicksand",sans-serif;font-weight:700;font-size:54px;color:var(--plum);letter-spacing:-1px;line-height:1}
.account-links{left:737px;top:25px;font-size:12px;display:flex;line-height:16px}
.account-links a{color:#555;text-decoration:none;padding:0 9px;border-left:1px solid #d4d4d4}
.account-links a:first-child{border-left:none;padding-left:0}
.account-links a.is-hover{color:var(--plum);text-decoration:underline}
.cart{left:935px;top:24px;font-size:12px;color:#555;display:flex;align-items:center;gap:4px;line-height:16px}
.cart b{color:var(--green);font-weight:400}
.call{left:539px;top:69px;font-size:21px;color:#444;display:flex;align-items:center;gap:8px;white-space:nowrap}
.call strong{color:var(--green)}
.search{left:855px;top:70px;width:150px;height:24px;background:#ececec;border:1px solid #dcdcdc;font-size:12px;color:#999;padding:4px 8px}
.search svg{position:absolute;right:6px;top:5px}
.main-nav{left:538px;top:113px;width:467px;height:31px;border:1px solid #d8d8d8;background:var(--white);display:flex;font-family:"Quicksand",sans-serif;font-weight:500;font-size:15px}
.main-nav span{color:#333;text-align:center;line-height:29px}
.main-nav .active{background:var(--plum);color:var(--white)}

/* breadcrumb */
.breadcrumb{left:112px;top:204px;font-size:13px;color:#444;display:flex;gap:12px}
.breadcrumb .current{color:var(--plum)}

/* form */
.section-title{font-family:"Quicksand",sans-serif;font-weight:700;font-size:21px;color:#333}
.label{font-size:12px;color:#555}
.field{height:26px;background:var(--field);border:1px solid var(--field-line)}
.field.error{background:#f6f0f0;border:2px solid var(--error)}
.submit{left:116px;top:658px;width:130px;height:32px;background:var(--plum);color:var(--white);font-size:13px;display:flex;align-items:center;justify-content:center;gap:12px}

/* total */
.ornament{left:702px;top:231px;width:176px;height:455px;background:linear-gradient(180deg,#f3f3f3,#fafafa 70%,#ffffff);border-radius:90px 90px 10px 10px}
.total-label{left:825px;top:318px;font-family:"Niconne",cursive;font-size:30px;color:var(--green)}
.total-value{left:825px;top:350px;font-family:"Niconne",cursive;font-size:50px;color:var(--green)}
.total-note{left:829px;top:408px;font-size:12px;color:var(--muted)}

/* footer */
.site-footer{left:0;top:798px;width:1117px;height:335px;background:var(--plum-deep)}
.footer-title{font-family:"Quicksand",sans-serif;font-weight:700;font-size:20px;color:var(--white)}
.footer-list{left:112px;top:922px;width:200px;list-style:none;font-size:12px;color:var(--white)}
.footer-list li{height:35px;line-height:22px;border-bottom:1px solid rgba(255,255,255,.12);padding-left:14px;position:relative}
.footer-list li::before{content:"";position:absolute;left:2px;top:9px;width:4px;height:4px;border-radius:50%;background:var(--white)}
.social{left:479px;width:200px;display:flex;align-items:center;gap:11px;font-family:"Quicksand",sans-serif;font-weight:500;font-size:17px;color:var(--white)}
.social i{display:block;width:29px;height:29px;background:rgba(255,255,255,.35);border-radius:3px}
.newsletter{left:761px;top:913px;width:244px;height:25px;background:var(--white);font-size:12px;color:#777;padding:5px 10px}
.newsletter .go{position:absolute;right:0;top:0;width:33px;height:25px;border-left:1px solid #ccc;display:flex;align-items:center;justify-content:center}
.footer-legal{left:761px;top:1040px;font-size:12px;color:var(--white);line-height:16px}
.bottom-bar{left:0;top:1133px;width:1117px;height:67px;background:var(--white)}
.bottom-copy{left:112px;top:1155px;font-size:12px;color:var(--plum)}
.payment{left:788px;top:1155px;font-size:12px;color:var(--plum)}
.cards{left:889px;top:1151px;display:flex;gap:3px}
.cards i{display:block;width:27px;height:18px;border-radius:2px;background:var(--card)}
</style>
</head>
<body>
<div class="abs top-rule"></div>
<header class="abs site-header"></header>
<div class="abs brand"><span class="brand-name">Velmora</span><span class="brand-mark"></span></div>

<nav class="abs account-links">
  <a href="#">My Checkout</a><a href="#" class="is-hover">Login</a><a href="#">Register</a>
</nav>
<div class="abs cart">
  <svg width="18" height="16" viewBox="0 0 18 16"><path d="M1 2h3l2 9h9l2-7H5" fill="none" stroke="#7ab317" stroke-width="2"/><circle cx="7" cy="14" r="1.5" fill="#7ab317"/><circle cx="14" cy="14" r="1.5" fill="#7ab317"/></svg>
  Cart : <b>00</b>
</div>
<div class="abs call">
  <svg width="22" height="16" viewBox="0 0 22 16"><path d="M2 6c0-3 4-4 9-4s9 1 9 4l-1 2h-4l-1-2H8L7 8H3z M5 9h12l2 6H3z" fill="#7ab317"/></svg>
  <span><strong>Call Us</strong> : 91+011- 4827 1690</span>
</div>
<div class="abs search">Search
  <svg width="12" height="12" viewBox="0 0 12 12"><circle cx="5" cy="5" r="3.5" fill="none" stroke="#aaa" stroke-width="1.5"/><path d="M8 8l3 3" stroke="#aaa" stroke-width="1.5"/></svg>
</div>
<nav class="abs main-nav">
  <span class="active" style="width:76px">Home</span><span style="width:60px">About</span><span style="width:86px">Services</span><span style="width:80px">Products</span><span style="width:72px">Specials</span><span style="width:91px">Contact</span>
</nav>

<div class="abs breadcrumb">
  <span>Home</span><span>&gt;</span><span>Products</span><span>&gt;</span><span>My Shopping Cart</span><span>&gt;</span><span class="current">Checkout</span>
</div>

<h2 class="abs section-title" style="left:112px;top:268px">Your Email Address</h2>
<div class="abs label" style="left:113px;top:305px">Email ID</div>
<div class="abs field error" style="left:113px;top:322px;width:243px"></div>
<div class="abs label" style="left:404px;top:305px">Password</div>
<div class="abs field" style="left:404px;top:322px;width:243px"></div>

<h2 class="abs section-title" style="left:112px;top:400px">Your Billing / Contact Details</h2>
<div class="abs label" style="left:114px;top:440px">First Name</div>
<div class="abs field" style="left:114px;top:455px;width:242px"></div>
<div class="abs label" style="left:406px;top:440px">Last Name</div>
<div class="abs field" style="left:406px;top:455px;width:242px"></div>
<div class="abs label" style="left:114px;top:492px">Address</div>
<div class="abs field" style="left:114px;top:507px;width:242px"></div>
<div class="abs label" style="left:406px;top:492px">City</div>
<div class="abs field" style="left:406px;top:507px;width:242px"></div>
<div class="abs label" style="left:114px;top:541px">Country</div>
<div class="abs field" style="left:114px;top:555px;width:242px"></div>
<div class="abs label" style="left:406px;top:541px">Post Code</div>
<div class="abs field" style="left:406px;top:555px;width:242px"></div>
<div class="abs label" style="left:116px;top:595px">Phone Number</div>
<div class="abs field" style="left:116px;top:610px;width:243px"></div>
<div class="abs submit">Submit Now
  <svg width="8" height="12" viewBox="0 0 8 12"><path d="M1 1l5 5-5 5" fill="none" stroke="#fff" stroke-width="2"/></svg>
</div>

<div class="abs ornament" role="img" aria-label="Faint flower stem and spiral ornament"></div>
<div class="abs total-label">Total Amount</div>
<div class="abs total-value">$ 1138</div>
<div class="abs total-note">(Excluding shipping and tax)</div>

<footer class="abs site-footer"></footer>
<h3 class="abs footer-title" style="left:112px;top:876px">Browse Velmora</h3>
<ul class="abs footer-list">
  <li>Home</li><li>About Us</li><li>Our Product</li><li>Contacts Us</li>
</ul>
<h3 class="abs footer-title" style="left:476px;top:876px">Velmora Social</h3>
<div class="abs social" style="top:922px"><i></i>FOLLOW US</div>
<div class="abs social" style="top:967px"><i></i>BECOME FAN</div>
<div class="abs social" style="top:1012px"><i></i>JOIN US</div>
<h3 class="abs footer-title" style="left:761px;top:876px">Newsletter Subscribe</h3>
<div class="abs newsletter">Email Address
  <span class="go"><svg width="16" height="16" viewBox="0 0 16 16"><circle cx="8" cy="8" r="8" fill="#7d1760"/><path d="M6 4l4 4-4 4" fill="none" stroke="#fff" stroke-width="2"/></svg></span>
</div>
<div class="abs footer-legal">All Right Reserved Copyright © 2012<br>Privacy Policy &nbsp;|&nbsp; Terms of Us</div>

<div class="abs bottom-bar"></div>
<div class="abs bottom-copy">All Right Reserved Copyright © 2012 | Privacy Policy &nbsp;|&nbsp; Terms of Us</div>
<div class="abs payment">Payment Iptions</div>
<div class="abs cards"><i></i><i></i><i></i><i></i></div>
</body>
</html>
```